Buch-/eBook-Cover für Traumatherapeutin
Zielgruppe
Ich bin Traumatherapeutin und schreibe ein Buch zum Thema Trauma bearbeiten.
Meine Zielgruppe sucht Heilung, Genesung, Selbstliebe etc.
Aufgabenstellung
Buchcover
Bitte erstell mir ein modernes positives inspirierendes Buchcover mit dem
Titel: 'Morgens LEISE aufbrechen“
Untertitel: „Geh den Pfad, der dich leise ruft“
Dr. Merle Kuhnast
Ich hätte gerne ein modernes Buch, das entweder einen Bezug zum Thema Trauma hat oder aber einfach stylische Schriftzüge. Bin aber auch offen für andere Vorschläge.
Dunkelblau, weiß und türkis oder auch rosa mag ich ganz gerne. Wobei Dunkelblau, weiß und türkis meine Favoriten sind und mit rosa höchstens kleinere Akzente gesetzt werden sollten.
Das Buchcover soll modern sein und direkt ansprechen. Gerne eine originelle Lösung, oder etwas Besonderes, etwas das Tiefe ausdrückt, oder man mehrmals hinsehen muss um etwas zu erkennen oder etwas das mehr Interpretationsspielraum lässt.
Gerne auch viel weiß, zumindest heller und nicht zu dunkel. Stylish, aber nicht überfrachtet.
Schreib mich gerne an, wenn du Fragen hast.
Ich habe mal zwei Beispiel von Typolösungen angehängt, die ich ganz cool fände.
Ich freue mich auf deine Ideen :-)
Ganz liebe Grüße
Merle

```html
<!DOCTYPE html>
<html lang="de">
<head>
<meta charset="UTF-8">
<title>Morgens LEISE aufbrechen – Buchcover</title>
<link rel="stylesheet" href="https://fonts.googleapis.com/css2?family=Bebas+Neue&family=Open+Sans:ital,wght@0,400;1,400&family=Sacramento&display=swap">
<style>
  :root {
    --mint: #a9d8d3;
    --deep-teal: #1d6b5c;
    --white: #ffffff;
  }
  html, body {
    margin: 0;
    padding: 0;
    width: 858px;
    height: 1200px;
    overflow: hidden;
    background: var(--mint);
  }
  .cover {
    position: relative;
    width: 858px;
    height: 1200px;
    background: var(--mint);
    overflow: hidden;
  }
  .author {
    position: absolute;
    top: 48px;
    left: 0;
    width: 100%;
    text-align: center;
    margin: 0;
    font-family: "Open Sans", sans-serif;
    font-weight: 400;
    font-size: 26px;
    color: var(--white);
    letter-spacing: 0.2px;
  }
  .title {
    margin: 0;
    font-weight: normal;
  }
  .title-script {
    position: absolute;
    font-family: "Sacramento", cursive;
    color: var(--deep-teal);
    line-height: 1;
    white-space: nowrap;
  }
  .title-top {
    left: 100px;
    top: 370px;
    font-size: 140px;
  }
  .title-main {
    position: absolute;
    left: 0;
    top: 488px;
    width: 100%;
    text-align: center;
    font-family: "Bebas Neue", sans-serif;
    font-size: 222px;
    line-height: 1;
    color: var(--white);
    letter-spacing: 1px;
  }
  .title-bottom {
    right: 82px;
    top: 640px;
    font-size: 130px;
  }
  .subtitle {
    position: absolute;
    right: 112px;
    top: 764px;
    margin: 0;
    text-align: right;
    font-family: "Open Sans", sans-serif;
    font-style: italic;
    font-size: 26px;
    line-height: 36px;
    color: var(--deep-teal);
  }
</style>
</head>
<body>
  <main class="cover">
    <p class="author">Dr. Merle Kuhnast</p>
    <h1 class="title">
      <span class="title-script title-top">Morgens</span>
      <span class="title-main">LEISE</span>
      <span class="title-script title-bottom">aufbrechen</span>
    </h1>
    <p class="subtitle">Geh den Pfad, der dich<br>leise ruft</p>
  </main>
</body>
</html>
```